Vexolab Cholesterol Rapid Test

We need a new Packaging for an old product named The Vexolab™ Cholesterol Test. Something fresh, modern, without forgetting that it is a medical product.
The Vexolab™ Cholesterol test is a complete, disposable, 3 minute test intended for use for early detection of elevated blood cholesterol levels associated with increased risk of coronary artery disease.

Target Market(s)

Pharmacy stores, Government.

Industry/Entity Type

Pharmaceutical

Logo Text

3 Minute Test

Font styles to use
Sans Serif

Requirements
Must have
• We need a new image, fresh, modern, without forgetting that it is a medical product.
Nice to have
• 1.- Security and confidence when the test is performed.
• 2.- Only one drop of blood is needed.
• 3.- Just 3 minutes for the result.
• 4.- Emphasize that the test can be done from the comfort of your home

```html
<!DOCTYPE html>
<html lang="en">
<head>
<meta charset="utf-8">
<title>Vexolab Cholesterol Rapid Test – Packaging</title>
<link href="https://fonts.googleapis.com/css2?family=Montserrat:wght@400;500;700&display=swap" rel="stylesheet">
<style>
  :root {
    --red: #ed1c24;
    --red-deep: #b5162a;
    --navy: #28245e;
    --ink: #3a3a3c;
    --paper: #ffffff;
    --stage-light: #ffffff;
    --stage-mid: #f0f0f0;
    --pattern-grey: #ececed;
    --rule-grey: #bdbdbd;
    --tab-dark: #3d3d3f;
  }
  html, body {
    margin: 0;
    padding: 0;
    overflow: hidden;
  }
  body {
    width: 1067px;
    height: 1200px;
    position: relative;
    font-family: "Montserrat", sans-serif;
    background: linear-gradient(135deg, var(--stage-mid) 0%, var(--stage-light) 45%, var(--stage-light) 100%);
  }
  .card {
    position: absolute;
    top: 115px;
    width: 423px;
    height: 746px;
    background: var(--paper);
    box-shadow: 0 2px 10px rgba(0,0,0,0.12);
    overflow: hidden;
  }
  .card--front { left: 97px; }
  .card--back { left: 548px; }

  .cut-line {
    position: absolute;
    top: 32px;
    left: 20px;
    right: 20px;
    height: 0;
    border-top: 2px dashed var(--rule-grey);
  }
  .cut-line__scissors {
    position: absolute;
    left: 72px;
    top: -13px;
    background: var(--paper);
    padding: 0 4px;
    font-size: 20px;
    line-height: 24px;
    color: var(--ink);
  }

  .brand-name {
    position: absolute;
    left: 0;
    right: 0;
    text-align: center;
    color: var(--red);
    font-weight: 400;
    letter-spacing: 0.5px;
  }
  .brand-name sup { font-size: 0.35em; vertical-align: super; }

  .card--front .brand-name { top: 176px; font-size: 30px; }

  .hero-drop-area {
    position: absolute;
    left: 66px;
    top: 218px;
    width: 294px;
    height: 487px;
    border-radius: 147px 147px 147px 147px / 240px 240px 147px 147px;
    background: radial-gradient(circle at 50% 72%, var(--red-deep) 0%, var(--red) 55%, var(--red) 100%);
  }
  .hero-pattern-area {
    position: absolute;
    left: 0;
    right: 0;
    bottom: 0;
    height: 228px;
    background: linear-gradient(180deg, rgba(236,236,237,0) 0%, var(--pattern-grey) 35%, var(--pattern-grey) 100%);
  }
  .hero-title {
    position: absolute;
    left: 66px;
    width: 294px;
    top: 494px;
    margin: 0;
    text-align: center;
    color: var(--paper);
    font-size: 32px;
    font-weight: 400;
    line-height: 44px;
  }

  .test-area {
    position: absolute;
    left: 121px;
    top: 69px;
    width: 174px;
    height: 174px;
  }
  .faint-backdrop {
    position: absolute;
    left: 60px;
    top: 250px;
    width: 300px;
    height: 430px;
    border-radius: 150px;
    background: radial-gradient(circle at 50% 60%, #f3f3f4 0%, rgba(243,243,244,0) 70%);
  }
  .card--back .brand-name { top: 342px; font-size: 21px; }
  .product-name {
    position: absolute;
    top: 364px;
    left: 0;
    right: 0;
    margin: 0;
    text-align: center;
    color: var(--ink);
    font-size: 32px;
    font-weight: 400;
  }
  .result-window {
    position: absolute;
    top: 425px;
    width: 164px;
    height: 181px;
    border: 1.5px solid var(--ink);
    background: var(--paper);
    box-sizing: border-box;
  }
  .result-window--control { left: 29px; }
  .result-window--sample { left: 223px; }
  .timer {
    position: absolute;
    top: 608px;
    left: 0;
    right: 0;
    text-align: center;
    color: var(--ink);
    font-size: 33px;
  }
  .pull-tab {
    position: absolute;
    left: 23px;
    top: 661px;
    width: 400px;
    height: 48px;
  }

  .brand-signature {
    position: absolute;
    left: 700px;
    width: 360px;
    top: 1088px;
    text-align: center;
    color: var(--red);
    font-size: 43px;
    font-weight: 400;
    letter-spacing: 1px;
  }
  .brand-signature sup { font-size: 0.3em; vertical-align: super; }
</style>
</head>
<body>

  <section class="card card--front" aria-label="Pack front">
    <div class="cut-line"><span class="cut-line__scissors">✂</span></div>
    <div class="brand-name">Vexolab<sup>™</sup></div>
    <div class="hero-pattern-area" role="img" aria-label="Soft grey pattern of small blood drops"></div>
    <div class="hero-drop-area" role="img" aria-label="Large red blood drop illustration"></div>
    <h1 class="hero-title">cholesterol<br>test</h1>
  </section>

  <section class="card card--back" aria-label="Test card">
    <div class="cut-line"><span class="cut-line__scissors">✂</span></div>

    <svg class="test-area" viewBox="0 0 174 174" aria-label="Test area">
      <defs>
        <path id="ring-top" d="M 25 87 A 62 62 0 0 1 149 87"/>
        <path id="ring-bottom" d="M 18 87 A 69 69 0 0 0 156 87"/>
      </defs>
      <circle cx="87" cy="87" r="87" fill="var(--navy)"/>
      <circle cx="87" cy="87" r="27" fill="#ffffff"/>
      <g stroke="var(--red)" stroke-width="2">
        <line x1="87" y1="4" x2="87" y2="30"/>
        <line x1="87" y1="144" x2="87" y2="170"/>
        <line x1="4" y1="87" x2="30" y2="87"/>
        <line x1="144" y1="87" x2="170" y2="87"/>
      </g>
      <g fill="#ffffff" font-family="Montserrat, sans-serif" font-weight="700" font-size="17" letter-spacing="2">
        <text><textPath href="#ring-top" startOffset="25%" text-anchor="middle">TEST</textPath></text>
        <text><textPath href="#ring-top" startOffset="75%" text-anchor="middle">AREA</textPath></text>
        <text><textPath href="#ring-bottom" startOffset="25%" text-anchor="middle">TEST</textPath></text>
        <text><textPath href="#ring-bottom" startOffset="75%" text-anchor="middle">AREA</textPath></text>
      </g>
    </svg>

    <div class="faint-backdrop" role="img" aria-label="Faint grey blood drop watermark"></div>
    <div class="brand-name">Vexolab<sup>™</sup></div>
    <h2 class="product-name">cholesterol test</h2>
    <div class="result-window result-window--control"></div>
    <div class="result-window result-window--sample"></div>
    <div class="timer">3 min</div>

    <svg class="pull-tab" viewBox="0 0 400 48" aria-label="Pull tab">
      <polygon points="0,0 400,0 400,48 36,48" fill="var(--red)"/>
      <polygon points="0,0 48,8 36,48" fill="var(--tab-dark)"/>
      <polygon points="188,14 200,4 212,14 205,14 205,32 195,32 195,14" fill="#ffffff"/>
    </svg>
  </section>

  <div class="brand-signature">VEXOLAB<sup>™</sup></div>

</body>
</html>
```